Video Thumbnail Design for Jazz Piano YouTube channel

Hello, my name’s Marcus Fenwick. I run a jazz piano YouTube channel called ‘Keyhaven Lessons’ (www.vidstreamer.example/keyhavenlessons). It’s the most subscribed to jazz piano YouTube channel with over 200,000 subscribers.

I need a designer to create an eye-catching thumbnail, to be used for my upcoming videos.

BRIEF:
For now, I’m asking for just one thumbnail design. I will choose a designer from this initial project, and I plan to commission additional designs from the same designer - so that my thumbnails all have a coherent look.

WHAT MAKES A GOOD THUMBNAIL:
Above all, your thumbnail design must be EYE-CATCHING and STAND OUT. Imagine scrolling through hundreds of YouTube videos - the video’s thumbnail artwork is one of the key aspects that gets someone to click and watch a video, so this is a VERY important aspect to getting views.

Your design can be innovative - surprise me. I want your design to JUMP OUT at me. For example, you could experiment with creating a 3D effect, or having elements popping out of the frame. A YouTube thumbnail doesn’t have to be square to the edges - you can add white around the edges to create an unusual jagged effect (when viewed in YouTube's search, which has a white background), and certain things could come out of the picture (see attached files for reference).

Remember, YouTube thumbnails are displayed very small - especially on desktop. It’s a good idea to design your thumbnail at this small size, rather than at full size on your computer screen. You'll probably need to zoom in closer to my face and enlarge the text more than you normally would if you were creating a larger image.

Lots of contrast is needed in a tiny thumbnail. Blacks must be pitch black, whites must be white, color saturation - the thumbnail must contain a lot of energy in a small space.

A strong format for YouTube thumbnails is to have a FACE (my face) and TEXT (large white text, 3 - 5 words). You can use this if you like, or you can experiment with a different format. I’m completely open to your ideas.

BRAND LOOK & FEEL:
Here are some keywords that describe my brand:
- Calm
- Professional
- Sophisticated (jazz is a sophisticated style of music)
View my channel to see my visual style as a starting point: www.vidstreamer.example/keyhavenlessons

BRAND COLORS:
- Turquoise: Hex #00DBD7 (this is my main brand color and must be used in the thumbnail)
- Black
- White
- Red: #FC5B5B (I sometimes use this as a secondary color - you can use this in your design if you want, or not).

TEXT:
The font I use for my brand is ‘Lovelo’ (please use this font in your design - included in my attachment).
I like my text to be white against a black background.
For your design, you could use the text: 'SWEET CHORD VOICING' as sample text.

IMAGES:
I've attached several photos for you to work with - just choose one for your design. The backgrounds are not important to the Thumbnail - only me and the piano are needed - so it's up to you whether you black out the background, darken it, or leave it in. Feel free to zoom in, rotate at an angle, distort, etc.

SLANTS:
I like diagonal lines and slants - because they go well with the ‘jazz’ feel. This could include the text itself (at an angle instead of straight), or the picture (any images of me or the piano could be at an angle, rather than straight).

DIMENSIONS:
YouTube thumbnails must be 1280 pixels wide by 720 pixels tall. A ratio of 16:9 is ideal as it’s used most often in YouTube players and previews.

DELIVERABLES:
If your design is selected - I will need a Photoshop file delivered of the final design (this is so that I can edit the text myself to make it relevant to the video).

After that, I will commission further designs with you (these will be separate projects, each with its own payment). My end goal is to have 10 - 15 strong thumbnail designs - all from the same designer.

Thank you very much for your submission, I can't wait to see what you come up with!

Target Market(s)

My audience is 90% male, between 25 - 65 years old. I have viewers worldwide, but they mostly live in the US and Canada.

Font styles to use
Other font styles liked:
• Lovelo

Colors
31b7a3

Requirements
Must have
• Image and text (as described in the project description)
Nice to have
• Creative use of white edges to stand out on YouTube (against other traditional square looking thumbnails).
• See full description in the project description.

```html
<!DOCTYPE html>
<html lang="en">
<head>
<meta charset="utf-8">
<title>Sweet Chord Voicing – Keyhaven Lessons thumbnail</title>
<link href="https://fonts.googleapis.com/css2?family=Josefin+Sans:wght@700&family=Montserrat:wght@700&display=swap" rel="stylesheet">
<style>
  :root {
    --page-white: #ffffff;
    --pitch-black: #0a0a0a;
    --brand-turquoise: #00dbd7;
    --deep-teal: #169b95;
    --badge-grey: #2b2b2b;
    --title-white: #ffffff;
  }
  html, body {
    margin: 0;
    padding: 0;
    width: 1200px;
    height: 900px;
    overflow: hidden;
    background: var(--page-white);
  }
  .thumbnail {
    position: absolute;
    left: 289px;
    top: 257px;
    width: 621px;
    height: 350px;
  }
  .thumbnail-shapes {
    position: absolute;
    left: 0;
    top: 0;
    width: 621px;
    height: 350px;
    overflow: visible;
  }
  .backdrop { fill: var(--pitch-black); }
  .accent-band { fill: var(--brand-turquoise); }
  .accent-fold { fill: var(--deep-teal); }
  .title {
    position: absolute;
    left: 248px;
    top: 52px;
    width: 310px;
    margin: 0;
    text-align: center;
    font-family: "Josefin Sans", "Montserrat", sans-serif;
    font-weight: 700;
    font-size: 54px;
    line-height: 62px;
    letter-spacing: 1px;
    color: var(--title-white);
    text-transform: uppercase;
  }
  .duration-badge {
    position: absolute;
    left: 489px;
    top: 289px;
    width: 121px;
    height: 47px;
    border-radius: 5px;
    background: var(--badge-grey);
    color: var(--title-white);
    font-family: "Montserrat", sans-serif;
    font-weight: 700;
    font-size: 33px;
    line-height: 47px;
    text-align: center;
  }
</style>
</head>
<body>
  <div class="thumbnail">
    <svg class="thumbnail-shapes" viewBox="0 0 621 350" xmlns="http://www.w3.org/2000/svg">
      <defs>
        <linearGradient id="presenter-tones" x1="0" y1="0" x2="1" y2="1">
          <stop offset="0" stop-color="#e7b79c"/>
          <stop offset="0.45" stop-color="#9fe6de"/>
          <stop offset="0.8" stop-color="#6fc8c0"/>
          <stop offset="1" stop-color="#2a2a2a"/>
        </linearGradient>
      </defs>

      <!-- black panel with the jagged white corner at top left -->
      <polygon class="backdrop" points="0,200 160,110 175,33 230,33 280,0 621,0 621,350 0,350"/>

      <!-- turquoise slanted band, top left -->
      <polygon class="accent-band" points="0,160 155,72 166,33 226,33 252,72 351,0 290,0 260,30 226,0 170,0 150,40 0,110"/>
      <polygon class="accent-band" points="0,200 0,150 160,68 170,108"/>
      <polygon class="accent-fold" points="185,73 226,33 252,73"/>

      <!-- turquoise slanted band, bottom right -->
      <polygon class="accent-band" points="433,350 621,208 621,262 505,350"/>

      <!-- presenter at the piano -->
      <path role="img" aria-label="Photo of the presenter smiling up at the camera while seated at a digital piano"
            fill="url(#presenter-tones)"
            d="M40,30 C50,10 110,10 145,35 C160,60 160,110 150,135
               C190,150 205,190 210,245 L245,265
               L300,205 L370,175 L425,200 L430,260 L350,350
               L0,350 L0,215 C20,175 40,150 55,140
               C35,115 28,65 40,30 Z"/>
    </svg>

    <h1 class="title">Sweet<br>Chord<br>Voicing</h1>
    <div class="duration-badge">16:46</div>
  </div>
</body>
</html>
```